Bright Fern Accounting Postcard

I need a postcard that highlights my services and contact info. Please use the website for graphics/info... www.BrightFernAccounting.com

Target Market(s)

Business owners

Industry/Entity Type

Bookkeeper

Colors

Designer to choose colors to be used in the design.

Requirements
Must have
• Services listed, Certified Ledgerly Online Pro Advisor (can add Ledgerly logo), Contact info

```html
<!DOCTYPE html>
<html lang="en">
<head>
<meta charset="utf-8">
<title>Bright Fern Accounting Postcard</title>
<link rel="stylesheet" href="https://fonts.googleapis.com/css2?family=Raleway:wght@400;600;700;800&family=Open+Sans:wght@400;600;700&family=Merriweather:wght@400;700&display=swap">
<style>
:root{
  --navy:#0f3564;
  --navy-deep:#0a2a52;
  --steel:#c9ccd1;
  --badge:#d9dce0;
  --page:#e6e8eb;
  --white:#ffffff;
  --ink:#1b1b1b;
  --photo-a:#c9b8a6;
  --photo-b:#5d6f86;
}
*{margin:0;padding:0;box-sizing:border-box}
html,body{width:848px;height:1200px;overflow:hidden;background:var(--page)}
body{position:relative;font-family:"Open Sans",Arial,sans-serif}
.card{position:absolute;left:21px;width:806px;height:526px;background:var(--white);overflow:hidden;box-shadow:0 6px 14px rgba(0,0,0,.35)}
.card--front{top:40px}
.card--back{top:630px}
.shapes{position:absolute;inset:0}
.brand{position:absolute;display:flex;align-items:center;gap:8px;font-family:"Merriweather",Georgia,serif;font-weight:700;color:var(--navy)}
.brand__mark{width:22px;height:22px;background:var(--navy)}
.brand--front{left:22px;top:30px;font-size:23px}
.brand--back{left:408px;top:62px;font-size:21px}
.headline{position:absolute;left:22px;top:96px;color:var(--white);font-family:"Raleway",Arial,sans-serif;font-weight:800;line-height:1}
.headline__big{display:block;font-size:50px;letter-spacing:.5px}
.headline__small{display:block;font-size:28px;font-weight:700;margin-top:7px;letter-spacing:.3px}
.headline-rule{position:absolute;left:17px;top:191px;width:300px;height:1px;background:var(--white)}
.tagline{position:absolute;left:24px;top:200px;width:288px;text-align:center;color:var(--white);font-weight:600;font-size:12.5px;line-height:16px}
.services-label{position:absolute;left:0;top:262px;width:147px;height:27px;background:var(--steel);border-radius:0 14px 14px 0;padding-left:14px;font-family:"Raleway",Arial,sans-serif;font-weight:800;font-size:18px;line-height:27px;color:var(--navy)}
.services{position:absolute;left:14px;top:300px;list-style:none}
.services li{display:flex;align-items:center;gap:6px;height:37px;font-family:"Merriweather",Georgia,serif;font-size:15px;color:var(--navy);letter-spacing:.3px}
.services svg{width:28px;height:28px}
.credential{position:absolute;left:14px;top:413px;width:192px;font-family:"Merriweather",Georgia,serif;font-size:10px;line-height:13px;color:var(--ink)}
.credential-rule{position:absolute;left:210px;top:412px;width:1px;height:50px;background:#7b7b7b}
.partner-badge{position:absolute;left:222px;top:422px;width:140px;height:34px;border-radius:6px;background:var(--badge)}
.contact-line{position:absolute;left:14px;top:484px;height:42px;display:flex;align-items:center;gap:10px;color:var(--white);font-size:11px}
.contact-line span{display:flex;align-items:center;gap:5px}
.contact-line svg{width:12px;height:12px}
.photo{position:absolute;inset:0}
.offer__text{position:absolute;left:445px;top:16px;width:148px;text-align:center;color:var(--white);font-size:18px;line-height:23px}
.offer__stars{display:block;font-size:14px;letter-spacing:6px;margin:3px 0 4px}
.offer__price{display:block;font-weight:700;font-size:22px}
.cta{position:absolute;left:420px;top:480px;width:240px;text-align:center;color:var(--navy);font-weight:700;font-size:12.5px;line-height:15px}
.phone{position:absolute;left:675px;top:471px;height:55px;display:flex;align-items:center;gap:6px;color:var(--white);font-size:12.5px}
.phone svg{width:12px;height:12px}
.vision{position:absolute;left:0;top:22px;width:364px;text-align:center;color:var(--white)}
.vision__title{font-family:"Raleway",Arial,sans-serif;font-size:38px;font-weight:400;line-height:42px;letter-spacing:.5px}
.vision__title strong{font-weight:800}
.vision__rule{width:264px;height:1px;background:var(--white);margin:6px auto 10px}
.vision p{font-size:14px;line-height:16.5px;margin:0 auto 17px;width:324px}
.site{position:absolute;left:64px;top:473px;height:53px;display:flex;align-items:center;gap:7px;color:var(--navy);font-size:15px;letter-spacing:1px;font-weight:600}
.site svg{width:15px;height:15px}
.stamp{position:absolute;left:711px;top:22px;width:70px;height:85px;border:1.5px solid #444}
</style>
</head>
<body>

<section class="card card--front" aria-label="Postcard front">
  <svg class="shapes" viewBox="0 0 806 526" aria-hidden="true">
    <polygon points="0,85 382,85 322,259 0,259" fill="var(--navy)"/>
    <polygon points="0,484 383,484 394,526 0,526" fill="var(--navy)"/>
    <polygon points="412,0 424,0 334,259 406,526 394,526 322,259" fill="var(--steel)"/>
  </svg>
  <svg class="photo" viewBox="0 0 806 526" role="img" aria-label="Photo of four business professionals reviewing documents at a table">
    <defs>
      <linearGradient id="officeTone" x1="0" y1="0" x2="1" y2="1">
        <stop offset="0" stop-color="#e9e4de"/>
        <stop offset=".45" stop-color="var(--photo-a)"/>
        <stop offset="1" stop-color="var(--photo-b)"/>
      </linearGradient>
    </defs>
    <polygon points="441,0 806,0 806,471 407,471 351,259" fill="url(#officeTone)"/>
  </svg>
  <svg class="shapes" viewBox="0 0 806 526" aria-hidden="true">
    <polygon points="428,0 444,0 354,259 424,526 408,526 338,259" fill="var(--navy)"/>
    <polygon points="650,471 806,471 806,526 650,526 668,498" fill="var(--navy)"/>
    <path d="M445 0 H593 V177 L519 158 L445 177 Z" fill="var(--navy)"/>
    <path d="M452 0 V167 L519 150 L586 167 V0" fill="none" stroke="var(--white)" stroke-width="1.4" stroke-dasharray="4 3"/>
  </svg>

  <div class="brand brand--front"><span class="brand__mark"></span>Bright Fern Accounting</div>

  <h1 class="headline"><span class="headline__big">BOUTIQUE</span><span class="headline__small">ACCOUNTING FIRM</span></h1>
  <div class="headline-rule"></div>
  <p class="tagline">Specializing in Small Business Bookkeeping &amp; Payroll Processing with Ledgerly Online by Ardent.</p>

  <div class="services-label">SERVICES</div>
  <ul class="services">
    <li><svg viewBox="0 0 28 28"><g fill="var(--navy)"><ellipse cx="14" cy="7" rx="10" ry="4"/><rect x="4" y="9" width="20" height="4" rx="2"/><rect x="4" y="14" width="20" height="4" rx="2"/><rect x="4" y="19" width="20" height="4" rx="2"/></g></svg>BOOKKEEPING</li>
    <li><svg viewBox="0 0 28 28"><rect x="4" y="6" width="16" height="20" fill="var(--navy)"/><rect x="7" y="17" width="2.5" height="6" fill="#fff"/><rect x="11" y="13" width="2.5" height="10" fill="#fff"/><rect x="15" y="15" width="2.5" height="8" fill="#fff"/><circle cx="21" cy="7" r="5.5" fill="var(--navy)"/><text x="21" y="10" font-size="8" text-anchor="middle" fill="#fff" font-family="Arial">$</text></svg>FINANCIAL REPORTING</li>
    <li><svg viewBox="0 0 28 28"><g fill="var(--navy)"><circle cx="6" cy="9" r="3"/><circle cx="14" cy="7" r="3.5"/><circle cx="22" cy="9" r="3"/><rect x="3" y="13" width="6" height="11" rx="2"/><rect x="10.5" y="12" width="7" height="13" rx="2"/><rect x="19" y="13" width="6" height="11" rx="2"/></g></svg>PAYROLL PROCESSING</li>
  </ul>

  <p class="credential">Our Ledgerly Online Certified Professionals have the Knowledge and Expertise to Ensure Professional, Accurate, High Quality Service.</p>
  <div class="credential-rule"></div>
  <div class="partner-badge" role="img" aria-label="Certified partner badge"></div>

  <div class="contact-line">
    <span><svg viewBox="0 0 14 14"><rect x="1" y="3" width="12" height="8" fill="#fff"/><path d="M1 3 L7 8 L13 3" fill="none" stroke="var(--navy)" stroke-width="1.2"/></svg>info@brightfernaccounting.com</span>
    <span><svg viewBox="0 0 14 14"><g fill="none" stroke="#fff" stroke-width="1.1"><circle cx="7" cy="7" r="6"/><ellipse cx="7" cy="7" rx="2.6" ry="6"/><path d="M1 7 H13"/></g></svg>brightfernaccounting.com</span>
  </div>

  <p class="offer__text">Full Service Bookkeeping Starting at<span class="offer__stars">★★★</span><span class="offer__price">$395/MO.</span></p>

  <p class="cta">CONTACT US TODAY<br>for your no obligation quote!</p>
  <div class="phone"><svg viewBox="0 0 12 12"><path d="M2 1 L4.5 1 L5.5 3.5 L4 4.8 C4.8 6.5 5.5 7.2 7.2 8 L8.5 6.5 L11 7.5 L11 10 C6 11 1 6 2 1 Z" fill="#fff"/></svg>1.800.555.0142</div>
</section>

<section class="card card--back" aria-label="Postcard back">
  <svg class="shapes" viewBox="0 0 806 526">
    <defs>
      <linearGradient id="skylineTone" x1="0" y1="0" x2="0" y2="1">
        <stop offset="0" stop-color="var(--navy-deep)"/>
        <stop offset="1" stop-color="#1d4a80"/>
      </linearGradient>
    </defs>
    <polygon points="0,0 330,0 418,264 330,526 0,526" fill="url(#skylineTone)" role="img" aria-label="Faint city skyline photo under a navy overlay"/>
    <polygon points="0,473 348,473 330,526 0,526" fill="var(--steel)"/>
    <polygon points="342,0 356,0 444,264 356,526 342,526 430,264" fill="var(--navy)"/>
    <polygon points="360,0 368,0 456,264 368,526 360,526 448,264" fill="var(--steel)"/>
  </svg>

  <div class="vision">
    <h2 class="vision__title"><strong>OUR</strong> VISION</h2>
    <div class="vision__rule"></div>
    <p>At Bright Fern Accounting we have one mission in mind… to improve the quality, accuracy and efficiency of your business's back-end bookkeeping and payroll processing, so that you can focus on the nuts and bolts of your day to day operations.</p>
    <p>Founded by a former CFO in the San Francisco Bay Area, we bring a team of accounting professionals with over 20 years of expertise from one of the most competitive markets in the world.</p>
    <p>Our accounting firm grew from personal success in business financial management. We bring knowledge, insight and guidance to your business, offering value for time and money.</p>
    <p>From bookkeeping to financial reporting to payroll and beyond, we at Bright Fern Accounting have the expertise to provide your business with a comprehensive evaluation and easy to implement solutions.</p>
  </div>

  <div class="site"><svg viewBox="0 0 14 14"><g fill="none" stroke="var(--navy)" stroke-width="1.1"><circle cx="7" cy="7" r="6"/><ellipse cx="7" cy="7" rx="2.6" ry="6"/><path d="M1 7 H13"/></g></svg>brightfernaccounting.com</div>

  <div class="brand brand--back"><span class="brand__mark"></span>Bright Fern Accounting</div>
  <div class="stamp"></div>
</section>

</body>
</html>
```